Gutschein-Design für Verkauf von Online-Schmuckstücken
Zielgruppe
Wir verkaufen Online Schmuckstücke!
www.funkelreif-beispiel.de
Aufgabenstellung
Wir haben eine schwarze Schachtel erstellt und da drinne wird eine Geschenkgutschein sein:
Es soll sehr schlicht sein und schwarzen Hintergrund haben.
Vorderseite nur unser LOGO.
Rückseite:
Betrag: _________
Gültig Bis: _________
Code: __________
Und unten klein gedruckt steht:
Diese Karte ist gültig nur auf der online shop seite www.funkelreif-beispiel.de und in unserer offizielen Stores. Dieses Karte ist nicht gültig bei rabatierte Produkten und man kann nicht mit dieser karte einen Gutscheinkarte kaufen.
Der Design soll sehr schlicht und dezenz sein.

```html
<!DOCTYPE html>
<html lang="de">
<head>
<meta charset="utf-8">
<title>Funkelreif – Geschenkgutschein</title>
<link rel="stylesheet" href="https://fonts.googleapis.com/css2?family=Roboto:wght@400;700&display=swap">
<style>
  :root {
    --stage: #2b2927;
    --card: #1f1c1b;
    --card-edge: #141211;
    --field: #ffffff;
    --ink: #2a2a2a;
    --text-light: #f2f0ee;
    --accent-pink: #f2b8c6;
  }
  * { box-sizing: border-box; margin: 0; padding: 0; }
  html, body {
    width: 1200px;
    height: 800px;
    overflow: hidden;
  }
  body {
    background: var(--stage);
    font-family: "Roboto", sans-serif;
    display: flex;
    flex-direction: column;
    align-items: center;
    justify-content: center;
    gap: 40px;
  }
  .voucher-card {
    width: 720px;
    height: 340px;
    background: var(--card);
    box-shadow: 0 10px 24px rgba(0, 0, 0, 0.45);
    border-bottom: 4px solid var(--card-edge);
    position: relative;
  }

  /* Vorderseite */
  .voucher-front {
    display: flex;
    align-items: center;
    justify-content: center;
  }
  .brand {
    display: flex;
    align-items: center;
    gap: 18px;
  }
  .brand-dot {
    width: 52px;
    height: 52px;
    border-radius: 50%;
    background: var(--text-light);
  }
  .brand-name {
    font-size: 46px;
    font-weight: 400;
    color: var(--text-light);
    letter-spacing: 1px;
  }

  /* Rückseite */
  .voucher-back {
    padding: 48px 70px 0 70px;
  }
  .field-list {
    list-style: none;
    display: flex;
    flex-direction: column;
    gap: 14px;
  }
  .field {
    height: 54px;
    background: var(--field);
    display: flex;
    align-items: center;
    padding-left: 22px;
    font-size: 17px;
    color: var(--ink);
  }
  .fine-print {
    margin-top: 26px;
    text-align: center;
    font-size: 11px;
    line-height: 1.5;
    color: var(--text-light);
  }
  .fine-print .web {
    color: var(--accent-pink);
    font-weight: 700;
  }
</style>
</head>
<body>
  <section class="voucher-card voucher-front" aria-label="Vorderseite">
    <div class="brand">
      <span class="brand-dot"></span>
      <span class="brand-name">Funkelreif</span>
    </div>
  </section>

  <section class="voucher-card voucher-back" aria-label="Rückseite">
    <ul class="field-list">
      <li class="field">Betrag :</li>
      <li class="field">Gültig Bis :</li>
      <li class="field">Code :</li>
    </ul>
    <p class="fine-print">
      Diese Karte ist gültig nur auf der online shop seite <span class="web">www.funkelreif-beispiel.de</span> und in unserer offizielen Stores. Dieses Karte ist nicht<br>
      gültig bei rabatierte Produkten und man kann nicht mit dieser karte einen Gutscheinkarte kaufen.
    </p>
  </section>
</body>
</html>
```